Prepared Meal Delivery Website

Need a new modern design for a prepared meal delivery company that is hosted on Shopify.

Target Market(s)

Young Professionals

Industry/Entity Type

Prepared Meal Delivery Service

Number of Pages Required

5+ page

Requirements
Must have
• Use https://www.velmorafoods.com/ as an example
Nice to have
• Vibrant page with call to action obvious and repeated
Should not have
• Generic look, grays/white/black

```html
<!DOCTYPE html>
<html lang="en">
<head>
<meta charset="utf-8">
<title>Stride Meals — Peak Nutrition</title>
<link rel="stylesheet" href="https://fonts.googleapis.com/css2?family=Anton&family=Poppins:wght@400;500;600;700&display=swap">
<style>
:root{
  --orange:#ff7a1a;
  --orange-deep:#ff5a14;
  --orange-soft:#ffa04a;
  --ink:#111111;
  --text:#3a3a3a;
  --muted:#777777;
  --grey-bg:#f2f2f2;
  --line:#e4e4e4;
  --white:#ffffff;
  --peach:#fff1e6;
}
*{box-sizing:border-box;margin:0;padding:0}
html,body{width:1200px;height:4858px;overflow:hidden;background:var(--white)}
body{font-family:'Poppins',sans-serif;color:var(--text)}
.page{position:relative;width:1200px;height:4858px;overflow:hidden}
.abs{position:absolute}
.display{font-family:'Anton',sans-serif;color:var(--ink);text-transform:uppercase;letter-spacing:.5px;line-height:1.02;font-weight:400}
.photo{position:absolute}
.btn{position:absolute;display:flex;align-items:center;justify-content:center;font-weight:700;font-size:11px;text-transform:uppercase;letter-spacing:.2px;text-decoration:none}
.btn-orange{background:var(--orange-deep);color:var(--white)}
.btn-outline{background:var(--white);border:2px solid var(--ink);color:var(--ink)}
.btn-white{background:var(--white);color:var(--ink)}

/* header */
.brand{left:88px;top:22px;color:var(--ink);font-weight:600;font-size:22px;line-height:1;white-space:nowrap}
.nav a{position:absolute;top:24px;font-size:11px;font-weight:500;color:var(--ink);text-decoration:none;text-transform:uppercase}

/* hero */
.hero-title{left:88px;top:242px;font-size:63px}
.hero-sub{left:88px;top:376px;width:420px;font-size:13px;line-height:22px;color:var(--text)}
.partners{top:745px;left:190px;display:flex;gap:70px}
.partner{width:110px;height:40px;display:flex;align-items:center;gap:8px}
.partner i{display:block;width:34px;height:34px;background:#b9b9b9;border-radius:50%}
.partner b{display:block;width:62px;height:10px;background:#cfcfcf;border-radius:2px}

.center-title{left:0;width:1200px;text-align:center}

/* steps */
.step{position:absolute;top:1006px;width:276px;height:353px;background:var(--white);box-shadow:0 4px 14px rgba(0,0,0,.08)}
.step .photo{left:0;top:0;width:276px;height:211px}
.step h3{position:absolute;left:32px;top:240px;font-family:'Anton',sans-serif;font-weight:400;font-size:19px;color:var(--ink);text-transform:uppercase}
.step p{position:absolute;left:32px;top:270px;width:210px;font-size:12px;line-height:18px;color:var(--text)}

/* stats */
.decision-title{left:160px;top:1560px;font-size:42px;color:var(--white);line-height:1.05}
.decision-sub{left:160px;top:1704px;width:520px;font-size:13px;line-height:21px;color:var(--white)}
.stat-card{left:753px;top:1462px;width:275px;height:350px;background:var(--white);text-align:center}
.stat-num{font-family:'Anton',sans-serif;font-size:32px;color:var(--ink);position:absolute;left:0;width:100%;top:220px}
.stat-lbl{font-family:'Anton',sans-serif;font-size:16px;color:#8a8a8a;position:absolute;left:0;width:100%;top:266px;line-height:1.15}

/* testimonial */
.testi{left:172px;top:1868px;width:856px;height:519px;background:var(--white);box-shadow:0 8px 24px rgba(0,0,0,.08)}
.testi-title{left:0;width:856px;top:84px;text-align:center;font-size:40px}
.quote-mark{left:460px;top:200px}
.quote-text{left:464px;top:262px;width:345px;font-size:13px;line-height:23px;color:var(--text)}
.quote-name{left:464px;top:404px;font-weight:700;font-size:15px;color:var(--ink);letter-spacing:.5px}
.dots{left:464px;top:436px;display:flex;gap:6px}
.dots span{width:7px;height:7px;border-radius:50%;background:#d0d0d0}
.dots span:first-child{background:var(--orange-deep)}

/* experts */
.experts-title{left:88px;top:2572px;font-size:42px}
.experts-sub{left:88px;top:2703px;font-size:13px;color:var(--text)}
.expert{position:absolute;top:2500px;width:206px;height:259px;background:var(--white);box-shadow:0 4px 14px rgba(0,0,0,.08);text-align:center}
.expert .photo{left:0;top:0;width:206px;height:187px}
.expert h4{position:absolute;top:203px;width:100%;font-family:'Anton',sans-serif;font-weight:400;font-size:16px;color:var(--ink)}
.expert p{position:absolute;top:228px;width:100%;font-size:10px;color:var(--text)}

/* diet food */
.diet{left:0;top:2868px;width:1200px;height:453px;background:var(--grey-bg)}
.diet-title{top:3000px;font-size:42px}
.diet-sub{top:3100px;left:380px;width:440px;text-align:center;font-size:13px;line-height:22px}
.diet-tags{top:3150px;left:0;width:1200px;display:flex;justify-content:center;gap:18px;font-size:13px}

/* athletes */
.ath-title{left:155px;top:3555px;font-size:40px}
.ath-sub{left:155px;top:3614px;width:340px;font-size:13px;line-height:22px}
.ath{position:absolute;background:var(--white);box-shadow:0 4px 14px rgba(0,0,0,.1);text-align:center}
.ath .photo{left:0;top:0;width:100%;height:145px}
.ath h5{position:absolute;bottom:12px;width:100%;font-family:'Anton',sans-serif;font-weight:400;font-size:14px;color:var(--ink)}

/* pillars */
.mbs-title{top:3880px;font-size:42px}
.mbs-sub{top:3940px;left:270px;width:660px;text-align:center;font-size:13px;line-height:22px}
.pillar{position:absolute;top:4013px;width:144px;height:144px;border-radius:50%;background:var(--white);box-shadow:0 4px 16px rgba(0,0,0,.12);display:flex;align-items:center;justify-content:center}
.pillar-lbl{position:absolute;top:4170px;width:144px;text-align:center;font-family:'Anton',sans-serif;font-size:20px;color:var(--ink)}

/* cta */
.cta{left:255px;top:4268px;width:702px;height:140px;background:linear-gradient(90deg,var(--orange-deep),var(--orange))}
.cta-title{left:302px;top:4304px;font-size:33px;color:var(--white);line-height:1}

/* footer */
.footer{left:0;top:4425px;width:1200px;height:433px;background:var(--ink)}
.f-brand{left:88px;top:4612px;color:var(--white);font-weight:600;font-size:30px;line-height:1;white-space:nowrap}
.f-col h6{font-family:'Anton',sans-serif;font-weight:400;font-size:20px;color:var(--white);margin-bottom:8px}
.f-col a,.f-col p{display:block;color:#dcdcdc;font-size:11.5px;line-height:22.6px;text-decoration:none}
.f-icon{display:inline-block;width:10px;height:10px;background:var(--orange);border-radius:50%;margin-right:8px;vertical-align:middle}
.socials{display:flex;gap:12px;margin-top:6px}
.socials span{width:12px;height:12px;border-radius:50%;background:var(--white)}
.email-box{left:864px;top:4612px;width:247px;height:40px;background:#2a2a2a;border-bottom:1px solid #555;display:flex;align-items:center;padding-left:20px;font-size:11px;color:var(--white)}
.copy{top:4823px;font-size:12px;color:var(--white)}
.chat{left:1116px;top:4766px;width:60px;height:60px;border-radius:50%;background:var(--orange);display:flex;align-items:center;justify-content:center}
</style>
</head>
<body>
<div class="page">

  <svg class="abs" style="left:0;top:0" width="1200" height="4858" aria-hidden="true">
    <defs>
      <linearGradient id="orangeGrad" x1="0" y1="0" x2="1" y2="1">
        <stop offset="0" stop-color="#ff8a1f"/>
        <stop offset="0.6" stop-color="#ff6a16"/>
        <stop offset="1" stop-color="#ff4e10"/>
      </linearGradient>
    </defs>
    <polygon points="820,0 1200,0 1200,830 1020,560" fill="#f1f1f1"/>
    <polygon points="0,1085 1200,1380 1200,2132 0,2132" fill="url(#orangeGrad)"/>
    <polygon points="1200,1430 1200,1812 1030,1812 1030,1600" fill="#ffffff"/>
    <polygon points="0,3470 0,3880 420,3880" fill="#f4f4f4"/>
    <polygon points="1200,3340 1200,3880 880,3880" fill="#fff3ea"/>
  </svg>

  <!-- header -->
  <div class="abs brand">Stride Meals</div>
  <nav class="nav">
    <a style="left:404px">Meal Plans</a>
    <a style="left:511px">How It Works</a>
    <a style="left:638px">Resources</a>
    <a style="left:743px">Testimonials</a>
    <a style="left:864px">App</a>
    <a style="left:921px">FAQ</a>
  </nav>
  <svg class="abs" style="left:992px;top:20px" width="120" height="24" aria-label="Account, cart and menu">
    <circle cx="9" cy="7" r="4.5" fill="none" stroke="#111" stroke-width="1.6"/>
    <path d="M2 20c1-5 13-5 14 0z" fill="none" stroke="#111" stroke-width="1.6"/>
    <rect x="50" y="3" width="15" height="18" rx="2" fill="none" stroke="#111" stroke-width="1.6"/>
    <path d="M54 3v-2h7v2" fill="none" stroke="#111" stroke-width="1.6"/>
    <path d="M100 8h18M103 13h15M106 18h12" stroke="#111" stroke-width="1.8"/>
  </svg>

  <!-- hero -->
  <div class="photo" role="img" aria-label="Athlete in orange trainers stretching on the floor" style="left:505px;top:122px;width:695px;height:500px;background:radial-gradient(ellipse at 60% 55%,#d6a48a 0%,#5a4a46 40%,rgba(240,240,240,0) 70%)"></div>
  <div class="photo" role="img" aria-label="Bowl of grilled salmon with greens and rice" style="left:-30px;top:547px;width:200px;height:283px;border-radius:50%;background:radial-gradient(circle,#c9a26a 0%,#6d7a3a 45%,#1c1c1c 70%)"></div>
  <h1 class="abs display hero-title">Peak Nutrition.<br>Peak Performance.</h1>
  <p class="abs hero-sub">Get into the best shape of your life with delicious, science-backed meals designed for results.</p>
  <a class="btn btn-orange" style="left:88px;top:434px;width:159px;height:42px">Shop Meal Plans</a>
  <a class="btn btn-outline" style="left:257px;top:434px;width:156px;height:42px">Take The Quiz</a>
  <div class="abs partners" aria-label="Partner brands">
    <div class="partner"><i></i><b></b></div>
    <div class="partner"><i></i><b></b></div>
    <div class="partner"><i></i><b></b></div>
    <div class="partner"><i></i><b></b></div>
    <div class="partner"><i></i><b></b></div>
  </div>

  <!-- how it works -->
  <h2 class="abs display center-title" style="top:886px;font-size:42px">How The Stride Meals Lifestyle<br>Plan Works</h2>
  <div class="step" style="left:172px">
    <div class="photo" role="img" aria-label="Meal prep containers with fruit on orange background" style="background:linear-gradient(135deg,#ffa030,#f08a1a)"></div>
    <h3>Pick Your Meal Plan</h3>
    <p>Shop 9 different meal plan subscriptions build for the taste and results</p>
  </div>
  <div class="step" style="left:462px">
    <div class="photo" role="img" aria-label="Woman eating a salad in a bright kitchen" style="background:linear-gradient(135deg,#6d5a45,#c9a27a)"></div>
    <h3>We Do The Coaching</h3>
    <p>Receive support and guidance from our team of nutrition experts</p>
  </div>
  <div class="step" style="left:753px">
    <div class="photo" role="img" aria-label="Phone with tracking app beside fresh vegetables" style="background:linear-gradient(135deg,#e8ece6,#6f9a4c)"></div>
    <h3>Track Your Progress</h3>
    <p>Get personalized fitness goals and daily tracking in the app</p>
  </div>

  <!-- stats -->
  <h2 class="abs display decision-title">You're only one<br>decision away from an<br>entirely different life</h2>
  <p class="abs decision-sub">Stride Meals has helped thousands of customers and top athletes lose weight, gain muscle, and improve their health.</p>
  <div class="abs stat-card">
    <svg class="abs" style="left:102px;top:80px" width="72" height="66" aria-label="Weight icon">
      <circle cx="36" cy="8" r="6" fill="none" stroke="#111" stroke-width="3"/>
      <path d="M18 16h36l14 46H4z" fill="none" stroke="#111" stroke-width="3" stroke-linejoin="round"/>
      <text x="36" y="50" text-anchor="middle" font-family="Anton,sans-serif" font-size="20" fill="#111">KG</text>
    </svg>
    <div class="stat-num">3,823,825</div>
    <div class="stat-lbl">POUNDS LOST<br>(AS OF 8/4/2022)</div>
  </div>
  <div class="photo" role="img" aria-label="Black meal tray with salad and zucchini noodles" style="left:960px;top:1420px;width:240px;height:300px;background:radial-gradient(ellipse,#8aa64a 0%,#2b2b2b 60%,rgba(255,255,255,0) 72%)"></div>
  <div class="photo" role="img" aria-label="Bowl of yellow pasta" style="left:988px;top:1405px;width:70px;height:68px;border-radius:50%;background:radial-gradient(circle,#f2d84a,#d9b824)"></div>

  <!-- testimonial -->
  <div class="photo" role="img" aria-label="Stacked meal prep containers" style="left:80px;top:2000px;width:100px;height:245px;border-radius:16px;background:linear-gradient(180deg,#7b8a3a,#2a2a2a 50%,#a45c2a)"></div>
  <div class="abs testi">
    <h2 class="abs display testi-title">Real People,<br>Real Transformations</h2>
    <div class="photo" role="img" aria-label="Customer before photo, shirtless" style="left:58px;top:196px;width:176px;height:263px;background:linear-gradient(180deg,#3d3d3d,#a07c66 55%,#2a2a2a)"></div>
    <div class="photo" role="img" aria-label="Customer after photo, shirtless" style="left:239px;top:196px;width:178px;height:263px;background:linear-gradient(180deg,#3d3d3d,#a88066 55%,#2a2a2a)"></div>
    <svg class="abs quote-mark" width="62" height="50" aria-hidden="true">
      <path d="M0 50V26C0 10 8 2 24 0v10c-8 2-11 7-11 14h11v26zM36 50V26C36 10 44 2 60 0v10c-8 2-11 7-11 14h11v26z" fill="#d9d9d9"/>
    </svg>
    <p class="abs quote-text">Lorem Ipsum is simply dummy text of the printing and typesetting industry. Lorem Ipsum has been the industry's standard dummy text ever since the 1500s, when an unknown printer took a galley of type and scrambled it to make a type specimen book. It has survived .</p>
    <div class="abs quote-name">JOHN SMITH</div>
    <div class="abs dots"><span></span><span></span><span></span></div>
  </div>

  <!-- experts -->
  <h2 class="abs display experts-title">Meal plans built<br>by experts and backed<br>by science</h2>
  <p class="abs experts-sub">Meet our team of experts</p>
  <div class="expert" style="left:557px">
    <div class="photo" role="img" aria-label="Expert stretching against a teal wall" style="background:linear-gradient(180deg,#2a8eaa,#1f7890)"></div>
    <h4>NAME HERE</h4><p>Nutrition &amp; content Director</p>
  </div>
  <div class="expert" style="left:776px">
    <div class="photo" role="img" aria-label="Expert holding a rope in a gym" style="background:linear-gradient(180deg,#f2f2f2,#8a8a8a)"></div>
    <h4>NAME HERE</h4><p>Nutrition &amp; content Director</p>
  </div>
  <div class="expert" style="left:994px">
    <div class="photo" role="img" aria-label="Expert measuring her waist" style="background:linear-gradient(180deg,#9a9a9a,#6e6e6e)"></div>
    <h4>NAME HERE</h4><p>Nutrition &amp; content Director</p>
  </div>

  <!-- diet food -->
  <div class="abs diet"></div>
  <div class="photo" role="img" aria-label="Meal trays with salmon and salad" style="left:0;top:2868px;width:300px;height:453px;background:radial-gradient(ellipse at 30% 40%,#c9895a 0%,#5c7a34 35%,#1e1e1e 60%,rgba(242,242,242,0) 75%)"></div>
  <div class="photo" role="img" aria-label="Meal tray with egg salad and soup bowl" style="left:900px;top:2868px;width:300px;height:453px;background:radial-gradient(ellipse at 60% 40%,#e6d36a 0%,#6b8a3c 35%,#1e1e1e 60%,rgba(242,242,242,0) 75%)"></div>
  <div class="photo" role="img" aria-label="Meal bowls at bottom edge" style="left:670px;top:3240px;width:220px;height:81px;background:radial-gradient(ellipse at 50% 100%,#6b8a3c 0%,#222 50%,rgba(242,242,242,0) 72%)"></div>
  <h2 class="abs display center-title diet-title">This isn't diet-food.<br>It's food-food</h2>
  <p class="abs diet-sub">Shop our macro balanced meal plans designed to get you results without the diet food taste.</p>
  <div class="abs diet-tags"><span>Clean</span><span>Vegan</span><span>Paleo</span><span>Keto</span><span>Classic</span><span>Meal Prep</span></div>
  <a class="btn btn-orange" style="left:521px;top:3178px;width:158px;height:43px">Shop Meal Plans</a>

  <!-- athletes -->
  <h2 class="abs display ath-title">We build athletes</h2>
  <p class="abs ath-sub">Stride Meals fuels the top athletes and fitness professionals in the game.</p>
  <a class="btn btn-orange" style="left:155px;top:3664px;width:177px;height:42px">Eat Like An Athlete</a>
  <div class="ath" style="left:655px;top:3419px;width:194px;height:185px">
    <div class="photo" role="img" aria-label="Athlete flexing in a gym" style="background:linear-gradient(180deg,#6a7a8a,#3a4550)"></div>
    <h5>JOHN SMITH</h5>
  </div>
  <div class="ath" style="left:655px;top:3619px;width:194px;height:196px">
    <div class="photo" role="img" aria-label="Athlete lifting a yellow weight plate" style="background:linear-gradient(180deg,#8a8a8a,#c9a42a)"></div>
    <h5>JOHN SMITH</h5>
  </div>
  <div class="ath" style="left:862px;top:3532px;width:193px;height:189px">
    <div class="photo" role="img" aria-label="Couple training together on a mat" style="background:linear-gradient(180deg,#e6e6e6,#9a9a9a)"></div>
    <h5>JOHN SMITH</h5>
  </div>

  <!-- pillars -->
  <h2 class="abs display center-title mbs-title">Mind. Body. Social.</h2>
  <p class="abs mbs-sub">Lorem Ipsum has been the industry's standard dummy text ever since the 1500s, when an unknown printer took a galley of type and scrambled it to make a type ...</p>
  <div class="pillar" style="left:368px" aria-label="Body icon">
    <svg width="60" height="60"><circle cx="30" cy="12" r="7" fill="none" stroke="#111" stroke-width="2"/><path d="M14 22h32l-4 18h-6v16h-12V40h-6z" fill="none" stroke="#111" stroke-width="2"/><path d="M24 30h12" stroke="#ff7a1a" stroke-width="3"/></svg>
  </div>
  <div class="pillar" style="left:528px" aria-label="Mind icon">
    <svg width="60" height="60"><path d="M30 6c12 0 20 9 20 19 0 6-3 10-6 13v16H26v-8h-8v-10l-6-4 6-8c0-10 6-18 12-18z" fill="none" stroke="#111" stroke-width="2"/><path d="M26 20c4 0 6 3 6 6s4 4 6 2" fill="none" stroke="#ff7a1a" stroke-width="2.5"/></svg>
  </div>
  <div class="pillar" style="left:690px" aria-label="Social icon">
    <svg width="60" height="60"><circle cx="12" cy="12" r="6" fill="none" stroke="#111" stroke-width="2"/><circle cx="48" cy="12" r="6" fill="none" stroke="#111" stroke-width="2"/><rect x="18" y="20" width="24" height="34" rx="3" fill="none" stroke="#111" stroke-width="2"/><rect x="24" y="28" width="12" height="14" fill="#ff7a1a"/></svg>
  </div>
  <div class="pillar-lbl" style="left:368px">BODY</div>
  <div class="pillar-lbl" style="left:528px">MIND</div>
  <div class="pillar-lbl" style="left:690px">SOCIAL</div>

  <!-- footer + cta -->
  <div class="abs footer"></div>
  <div class="abs cta"></div>
  <div class="photo" role="img" aria-label="Muscular man curling dumbbells" style="left:75px;top:4038px;width:255px;height:453px;border-radius:40%;background:radial-gradient(ellipse,#c49478 0%,#9a9a9a 45%,rgba(255,255,255,0) 70%)"></div>
  <h2 class="abs display cta-title">What are you<br>waiting for?</h2>
  <a class="btn btn-orange" style="left:585px;top:4321px;width:157px;height:42px;box-shadow:0 0 0 1px rgba(255,255,255,.2)">Shop Meal Plans</a>
  <a class="btn btn-white" style="left:751px;top:4321px;width:160px;height:42px">Take The Quiz</a>

  <div class="abs f-brand">Stride Meals</div>
  <div class="abs f-col" style="left:434px;top:4510px">
    <h6>ABOUT</h6>
    <a>Our Story</a><a>Nutrition &amp; Fitness</a><a>Health</a><a>Meals</a><a>Partners</a><a>Testimonials</a><a>How It Works</a><a>Press</a><a>Careers</a>
  </div>
  <div class="abs f-col" style="left:638px;top:4510px">
    <h6>CONTACT US</h6>
    <p><span class="f-icon"></span>123-456-7890</p>
    <p><span class="f-icon"></span>Live Chat 8-5 PST</p>
    <p><span class="f-icon"></span>info@stridemeals.com</p>
    <div class="socials" aria-label="Social links"><span></span><span></span><span></span><span></span></div>
  </div>
  <div class="abs f-col" style="left:864px;top:4510px;width:260px">
    <h6>JOIN OUR COMMUNITY</h6>
    <p style="line-height:21px">Sign up now and get expert nutrition advice delivered to your inbox weekly!</p>
  </div>
  <div class="abs email-box">Email Address
    <svg class="abs" style="right:14px;top:13px" width="14" height="14" aria-label="Send"><path d="M0 7L14 0 9 14 7 8z" fill="#ff7a1a"/></svg>
  </div>
  <div class="abs copy" style="left:88px">©Copyright 2022 | All Rights Reserved</div>
  <div class="abs copy" style="left:901px">Privacy Policy | Cookie Notice</div>
  <div class="abs chat" aria-label="Chat">
    <svg width="28" height="24"><path d="M2 2h24v15H12l-6 5v-5H2z" fill="#fff"/><circle cx="9" cy="10" r="1.6" fill="#ff7a1a"/><circle cx="14" cy="10" r="1.6" fill="#ff7a1a"/><circle cx="19" cy="10" r="1.6" fill="#ff7a1a"/></svg>
  </div>

</div>
</body>
</html>
```